Brisbane IT support business needs our first business card

Hello we are a Brisbane based Information Technology company providing support and services to small and medium sized businesses. We provide a range of services and solutions.

The business name is Wattlebrook Network Computing Services, or WNCS for short.

I am looking for a business card that looks professional (don't we all want that), but most importantly, it most utilize the colours in the logo attached.

Reason: Launched late, extending so people have enough time to actually submit something.

Target Market(s)

Other business owners seeking our IT services, and also home users.

Industry/Entity Type

Business

Requirements
Must have
• Please only use the blue/orange colours in logo attached

```html
<!DOCTYPE html>
<html lang="en">
<head>
<meta charset="utf-8">
<title>WNCS Business Card</title>
<link rel="stylesheet" href="https://fonts.googleapis.com/css2?family=Montserrat:wght@600;700&family=Didact+Gothic&display=swap">
<style>
  :root {
    --blue: #0f4a66;
    --orange: #d4741f;
    --paper: #f7f7f7;
    --ink: #2a2a2a;
    --stage: #3a3a3a;
  }
  * { margin: 0; padding: 0; box-sizing: border-box; }
  html, body { width: 1200px; height: 997px; overflow: hidden; }
  body { background: var(--stage); position: relative; font-family: "Didact Gothic", sans-serif; }

  .card {
    position: absolute;
    width: 620px; height: 354px;
    background: var(--paper);
    overflow: hidden;
    box-shadow: 0 10px 30px rgba(0,0,0,.45);
  }
  .card--front { left: 90px; top: 90px; }
  .card--back  { left: 490px; top: 540px; }

  .brand { position: absolute; display: flex; align-items: center; }
  .brand__mark { border-radius: 50%; background: var(--blue); flex: none; }
  .brand__rule { background: var(--orange); width: 2px; flex: none; }
  .brand__words { font-family: "Montserrat", sans-serif; font-weight: 700; color: var(--orange); line-height: 1; }
  .brand__short { display: block; letter-spacing: 1px; }
  .brand__long { display: block; text-transform: uppercase; }

  .card--front .brand { left: 70px; top: 97px; }
  .card--front .brand__mark { width: 160px; height: 160px; }
  .card--front .brand__rule { height: 110px; margin: 0 26px 0 30px; }
  .card--front .brand__short { font-size: 72px; }
  .card--front .brand__long { font-size: 12.5px; width: 190px; line-height: 1.15; margin-top: 4px; }

  .band { position: absolute; left: 0; top: 0; width: 100%; height: 84px; background: var(--blue); color: #fff; padding: 28px 0 0 32px; }
  .band__name { font-family: "Montserrat", sans-serif; font-weight: 700; font-size: 25px; letter-spacing: 1px; line-height: 1; }
  .band__role { font-family: "Montserrat", sans-serif; font-weight: 600; font-size: 14px; margin-top: 4px; }
  .strip { position: absolute; left: 0; bottom: 0; width: 100%; height: 14px; background: var(--orange); }

  .card--back .brand { left: 26px; top: 178px; }
  .card--back .brand__mark { width: 104px; height: 104px; }
  .card--back .brand__rule { height: 72px; margin: 0 16px 0 18px; }
  .card--back .brand__short { font-size: 44px; }
  .card--back .brand__long { font-size: 8px; width: 120px; line-height: 1.15; margin-top: 3px; }

  .contacts { position: absolute; left: 370px; top: 106px; list-style: none; }
  .contacts li { display: flex; align-items: center; height: 34px; font-size: 14px; color: var(--ink); }
  .contacts svg { width: 22px; height: 22px; margin-right: 16px; fill: var(--orange); flex: none; }
</style>
</head>
<body>

<section class="card card--front">
  <div class="brand">
    <span class="brand__mark"></span>
    <span class="brand__rule"></span>
    <span class="brand__words">
      <span class="brand__short">WNCS</span>
      <span class="brand__long">Wattlebrook Network Computing Services</span>
    </span>
  </div>
</section>

<section class="card card--back">
  <header class="band">
    <p class="band__name">DALE HORAN</p>
    <p class="band__role">Sports Therapist</p>
  </header>

  <div class="brand">
    <span class="brand__mark"></span>
    <span class="brand__rule"></span>
    <span class="brand__words">
      <span class="brand__short">WNCS</span>
      <span class="brand__long">Wattlebrook Network Computing Services</span>
    </span>
  </div>

  <ul class="contacts">
    <li>
      <svg viewBox="0 0 24 24" aria-hidden="true"><path d="M3 7c0-2 2-3 9-3s9 1 9 3v2h-5V7H8v2H3z"/><path d="M6 11h12l2 9H4z"/></svg>
      07700900418
    </li>
    <li>
      <svg viewBox="0 0 24 24" aria-hidden="true"><path d="M7 2h10a2 2 0 0 1 2 2v16a2 2 0 0 1-2 2H7a2 2 0 0 1-2-2V4a2 2 0 0 1 2-2zm0 3v13h10V5z"/></svg>
      01632 960214
    </li>
    <li>
      <svg viewBox="0 0 24 24" aria-hidden="true"><path d="M2 5h20v14H2z"/><path d="M2 5l10 8 10-8" fill="none" stroke="#f7f7f7" stroke-width="1.6"/></svg>
      dale@corvalistherapy.co.uk
    </li>
    <li>
      <svg viewBox="0 0 24 24" aria-hidden="true"><circle cx="12" cy="12" r="10"/></svg>
      @corvalistherapy
    </li>
    <li>
      <svg viewBox="0 0 24 24" aria-hidden="true"><circle cx="12" cy="12" r="10"/><path d="M2 12h20M12 2c3 3 3 17 0 20M12 2c-3 3-3 17 0 20" fill="none" stroke="#f7f7f7" stroke-width="1.4"/></svg>
      www.corvalistherapy.co.uk
    </li>
  </ul>

  <div class="strip"></div>
</section>

</body>
</html>
```